3 Business Card designs for a company with multiple services

We are a company that has 3 main services:

1) Security - CCTV & Alarm Sepcialists
2) Broadcast - Broadcast Sales and Technical Services
3) Distribution - Quality Products, Quality Service

The broadcast service is for Video Broadcast.

I will include our logos for each service.

I would like to also create a business card design for 7QK in general (see main logo).

Each card will be two-sided. On the front I would think it would include Logo, Name, Posistion and Mobile (and possibly email). And possibly our main number (which may be something like 1800 639 415)

On the back it MUST include a "lined" section to be able to write short quotes / prices.

Then include more details like Phone: 1800 639 415 Fax: 1800 639 412 Postal: PO Box 731, Tallowen, QLD Australia 4290 Website: www.7qk.com.au

We would like a fresh, inovative card design with that "wow check this out" feel about it.

Look forward to seeing what you can do! :)

Corey

Industry/Entity Type

Business

Requirements
Must have
• Quote section on the back!
Editable files.

```html
<!DOCTYPE html>
<html lang="en">
<head>
<meta charset="utf-8">
<title>7QK Business Cards – Fronts and Quote Backs</title>
<link rel="stylesheet" href="https://fonts.googleapis.com/css2?family=Arimo:wght@400;700&family=Barlow+Condensed:wght@700&display=swap">
<style>
  :root {
    --ink: #3a3a3a;
    --ink-soft: #4a4a4a;
    --paper: #ffffff;
    --border: #333333;
    --rule: #3a3a3a;
    --general: #3a3a3a;
    --security: #8c8c8c;
    --broadcast: #e39b00;
    --distribution: #0b3f84;
    --lock-red: #d2232a;
    --camera-gold: #f2b700;
    --globe-blue: #2d6fc2;
  }
  * { box-sizing: border-box; margin: 0; padding: 0; }
  html, body {
    width: 848px; height: 1200px; overflow: hidden;
    background: var(--paper);
  }
  .sheet {
    position: relative; width: 900px; height: 1273px;
    transform: scale(0.94222); transform-origin: 0 0;
    font-family: "Arimo", Arial, sans-serif; color: var(--ink);
  }
  .card {
    position: absolute; width: 399px; height: 238px;
    border: 1px solid var(--border); background: var(--paper); overflow: hidden;
  }
  .card.front { left: 40px; }
  .card.back { left: 458px; }
  .row-1 { top: 81px; } .row-2 { top: 340px; } .row-3 { top: 602px; } .row-4 { top: 867px; }

  .general { --accent: var(--general); --art: linear-gradient(180deg, #6d6d6d, #d2a21a 50%, #2d6fc2); }
  .security { --accent: var(--security); --art: linear-gradient(160deg, #e0e0e0, var(--lock-red) 70%); }
  .broadcast { --accent: var(--broadcast); --art: linear-gradient(160deg, #ffe27a, var(--camera-gold) 60%, #3a4a6a); }
  .distribution { --accent: var(--distribution); --art: linear-gradient(160deg, #7fb4ea, var(--globe-blue) 55%, #f2c230); }

  /* Front: brand strip */
  .brand-strip { position: absolute; left: 12px; top: 12px; width: 66px; height: 212px; }
  .brand-block {
    position: absolute; left: 0; top: 0; width: 40px; height: 158px;
    background: var(--ink); border-radius: 4px 0 0 0;
    display: flex; align-items: center; justify-content: center;
  }
  .general .brand-block { height: 212px; align-items: flex-start; padding-top: 14px; border-radius: 4px 0 0 4px; }
  .brand-name {
    writing-mode: vertical-rl; transform: rotate(180deg);
    font-family: "Arimo", Arial, sans-serif; font-weight: 700; font-size: 30px;
    letter-spacing: 10px; color: var(--paper);
  }
  .service-band {
    position: absolute; left: 40px; top: 0; width: 26px; height: 158px;
    background: var(--accent); display: flex; align-items: center; justify-content: center;
  }
  .general .service-band { height: 212px; background: var(--paper); }
  .service-band span {
    writing-mode: vertical-rl; transform: rotate(180deg);
    font-family: "Barlow Condensed", "Arial Narrow", sans-serif; font-weight: 700;
    font-size: 15px; letter-spacing: 5px; color: var(--paper);
  }
  .general .service-band span { color: var(--ink); font-size: 11px; letter-spacing: 1.2px; }
  .service-art {
    position: absolute; left: 0; top: 158px; width: 66px; height: 54px;
    background: var(--art); border-radius: 0 0 0 10px;
  }
  .general .service-art { left: 6px; top: 110px; width: 28px; height: 94px; border-radius: 4px; }

  /* Front: name and details */
  .name-bar {
    position: absolute; left: 156px; top: 14px; width: 243px; height: 25px;
    background: var(--ink); display: flex; align-items: center; padding-left: 9px;
  }
  .name-bar h2 { font-size: 14.5px; font-weight: 700; color: var(--paper); }
  .role {
    position: absolute; left: 156px; top: 40px; width: 243px; height: 12px;
    background: var(--accent); color: var(--paper);
    font-size: 10px; line-height: 12px; padding-left: 8px;
  }
  .details {
    position: absolute; left: 157px; top: 67px; height: 115px;
    border-left: 2px solid var(--ink-soft); padding-left: 9px;
    font-size: 11.5px; line-height: 15.5px;
  }
  .details address { font-style: normal; margin-bottom: 13px; }
  .details dl { display: grid; grid-template-columns: 46px auto; }
  .details dt { font-weight: 700; }

  /* Back: quote panel */
  .quote-head { position: absolute; left: 12px; top: 14px; width: 387px; height: 37px; }
  .quote-top { position: absolute; left: 0; top: 0; width: 100%; height: 25px; background: var(--ink); border-radius: 4px 0 0 0; }
  .quote-band { position: absolute; left: 0; top: 25px; width: 100%; height: 12px; background: var(--accent); }
  .general .quote-band { background: var(--ink); }
  .quote-art {
    position: absolute; left: 0; top: 0; width: 38px; height: 37px;
    background: var(--art); border-radius: 4px 0 0 8px;
  }
  .general .quote-art { width: 60px; }
  .quote-brand {
    position: absolute; left: 46px; top: 2px; color: var(--paper);
    font-weight: 700; font-size: 19px; letter-spacing: 9px;
  }
  .general .quote-brand { left: 70px; }
  .quote-service {
    position: absolute; left: 46px; top: 26px; color: var(--paper);
    font-family: "Barlow Condensed", "Arial Narrow", sans-serif; font-weight: 700;
    font-size: 9px; letter-spacing: 3px; line-height: 11px;
  }
  .general .quote-service { left: 4px; letter-spacing: 0.6px; }
  .quote-title {
    position: absolute; left: 175px; top: 4px; color: var(--paper);
    font-weight: 700; font-size: 13px;
  }
  .date-box {
    position: absolute; left: 236px; top: 2px; width: 136px; height: 20px;
    background: var(--paper); border-radius: 3px; border: 1px solid var(--ink);
    font-size: 10px; line-height: 18px; padding-left: 4px; color: var(--ink);
  }
  .quote-lines { position: absolute; left: 12px; top: 82px; width: 372px; }
  .quote-lines li { list-style: none; height: 35px; border-top: 1.3px solid var(--rule); }
</style>
</head>
<body>
<main class="sheet">

  <!-- General -->
  <section class="card front row-1 general">
    <div class="brand-strip">
      <div class="brand-block"><span class="brand-name">7QK</span></div>
      <div class="service-band"><span>SECURITY - BROADCAST - DISTRIBUTION</span></div>
      <div class="service-art" role="img" aria-label="Service icons: globe, camera and padlock"></div>
    </div>
    <div class="name-bar"><h2>Lachlan Brenner</h2></div>
    <p class="role">Managing Director</p>
    <div class="details">
      <address>PO Box 731,<br>Tallowen, QLD 4290</address>
      <dl>
        <dt>Tel.</dt><dd>1800 639 415</dd>
        <dt>Fax.</dt><dd>1800 639 412</dd>
        <dt>Mobile.</dt><dd>0491 570 158</dd>
        <dt>Email.</dt><dd>lachlan@7qk.com.au</dd>
        <dt>Web.</dt><dd>www.7qk.com.au</dd>
      </dl>
    </div>
  </section>
  <section class="card back row-1 general">
    <div class="quote-head">
      <div class="quote-top"></div><div class="quote-band"></div>
      <div class="quote-art" role="img" aria-label="Service icons: padlock, camera and globe"></div>
      <span class="quote-brand">7QK</span>
      <span class="quote-service">SECURITY - BROADCAST - DISTRIBUTION</span>
      <span class="quote-title">QUOTE ...</span>
      <span class="date-box">Date: ____ / ____ /_____</span>
    </div>
    <ul class="quote-lines"><li></li><li></li><li></li><li></li><li></li></ul>
  </section>

  <!-- Security -->
  <section class="card front row-2 security">
    <div class="brand-strip">
      <div class="brand-block"><span class="brand-name">7QK</span></div>
      <div class="service-band"><span>SECURITY</span></div>
      <div class="service-art" role="img" aria-label="Red padlock icon"></div>
    </div>
    <div class="name-bar"><h2>Declan Ashby</h2></div>
    <p class="role">CCTV and Alarm Specialist</p>
    <div class="details">
      <address>PO Box 731,<br>Tallowen, QLD 4290</address>
      <dl>
        <dt>Tel.</dt><dd>1800 639 415</dd>
        <dt>Fax.</dt><dd>1800 639 412</dd>
        <dt>Mobile.</dt><dd>0491 570 158</dd>
        <dt>Email.</dt><dd>declan@7qk.com.au</dd>
        <dt>Web.</dt><dd>www.7qk.com.au</dd>
      </dl>
    </div>
  </section>
  <section class="card back row-2 security">
    <div class="quote-head">
      <div class="quote-top"></div><div class="quote-band"></div>
      <div class="quote-art" role="img" aria-label="Red padlock icon"></div>
      <span class="quote-brand">7QK</span>
      <span class="quote-service">SECURITY</span>
      <span class="quote-title">QUOTE ...</span>
      <span class="date-box">Date: ____ / ____ /_____</span>
    </div>
    <ul class="quote-lines"><li></li><li></li><li></li><li></li><li></li></ul>
  </section>

  <!-- Broadcast -->
  <section class="card front row-3 broadcast">
    <div class="brand-strip">
      <div class="brand-block"><span class="brand-name">7QK</span></div>
      <div class="service-band"><span>BROADCAST</span></div>
      <div class="service-art" role="img" aria-label="Broadcast video camera icon"></div>
    </div>
    <div class="name-bar"><h2>Grant Mellor</h2></div>
    <p class="role">Sales and Technical Services</p>
    <div class="details">
      <address>PO Box 731,<br>Tallowen, QLD 4290</address>
      <dl>
        <dt>Tel.</dt><dd>1800 639 415</dd>
        <dt>Fax.</dt><dd>1800 639 412</dd>
        <dt>Mobile.</dt><dd>0491 570 158</dd>
        <dt>Email.</dt><dd>grant@7qk.com.au</dd>
        <dt>Web.</dt><dd>www.7qk.com.au</dd>
      </dl>
    </div>
  </section>
  <section class="card back row-3 broadcast">
    <div class="quote-head">
      <div class="quote-top"></div><div class="quote-band"></div>
      <div class="quote-art" role="img" aria-label="Broadcast video camera icon"></div>
      <span class="quote-brand">7QK</span>
      <span class="quote-service">BROADCAST</span>
      <span class="quote-title">QUOTE ...</span>
      <span class="date-box">Date: ____ / ____ /_____</span>
    </div>
    <ul class="quote-lines"><li></li><li></li><li></li><li></li><li></li></ul>
  </section>

  <!-- Distribution -->
  <section class="card front row-4 distribution">
    <div class="brand-strip">
      <div class="brand-block"><span class="brand-name">7QK</span></div>
      <div class="service-band"><span>DISTRIBUTION</span></div>
      <div class="service-art" role="img" aria-label="Globe icon"></div>
    </div>
    <div class="name-bar"><h2>Rhys Calloway</h2></div>
    <p class="role">Distribution Specialist</p>
    <div class="details">
      <address>PO Box 731,<br>Tallowen, QLD 4290</address>
      <dl>
        <dt>Tel.</dt><dd>1800 639 415</dd>
        <dt>Fax.</dt><dd>1800 639 412</dd>
        <dt>Mobile.</dt><dd>0491 570 158</dd>
        <dt>Email.</dt><dd>rhys@7qk.com.au</dd>
        <dt>Web.</dt><dd>www.7qk.com.au</dd>
      </dl>
    </div>
  </section>
  <section class="card back row-4 distribution">
    <div class="quote-head">
      <div class="quote-top"></div><div class="quote-band"></div>
      <div class="quote-art" role="img" aria-label="Globe icon"></div>
      <span class="quote-brand">7QK</span>
      <span class="quote-service">DISTRIBUTION</span>
      <span class="quote-title">QUOTE ...</span>
      <span class="date-box">Date: ____ / ____ /_____</span>
    </div>
    <ul class="quote-lines"><li></li><li></li><li></li><li></li><li></li></ul>
  </section>

</main>
</body>
</html>
```